This is a book by, for and about bereaved parents and grandparents

I need a paperback size cover with front and back please...I have an example of a cover i had done myself and you will see a butterfly graphic within my Preface (My Story) which may be nice to include..or not.

Please feel free to explore your own psyche on this subject light and dark work accepted...love to see your concepts on this difficult subject.
thanks and good luck to you all!
Updates

Good Day Designer..I will post my current photo for the cover shortly and i cannot wait to see your great designs!

Apologies to you all for the delay in providing feedback ..I'm a little overwhelmed at the quality of your work and most likely will be adding a second and third place tonight when i finalize this project..thanks for your hard work and patience

thanks to all the designers for your heartfelt work on this project..it is so very personal to me and If i could afford it I'd pay you all ..do take care and thanks again for your submisions Marla .

https://www.linkverse.net/Where-the-Quiet-Gardens-Grow-Again-4830196527718354/?epa=SEARCH_BOX

Target Market(s)

Family of children who have died before their time especially those who've left parents and grandparents to grieve their loss of all ages.

Industry/Entity Type

Writer

Font styles to use
Serif
Sans Serif
Decorative
Script

Colors

Designer to choose colors to be used in the design.

Requirements
Must have
• feeling of loss and renewal important to end in hope and faith for future despite the years and months and days of pure agony
• my pic
• my name to be seen clearly on front of paperback
Nice to have
• maybe my butterfly graphic if it works with your concept?
• I would appreciate it if you read my Preface it 23 pages but I hope it will provide insight into the contents of the book thanks for your time and patience
Should not have
• Gravestones religous icons
• such as crosses etc

```html
<!DOCTYPE html>
<html lang="en">
<head>
<meta charset="utf-8">
<title>Where the Quiet Gardens Grow Again – Paperback Cover</title>
<link rel="stylesheet" href="https://fonts.googleapis.com/css2?family=Kaushan+Script&family=Questrial&display=swap">
<style>
  :root {
    --page-bg: #f1f1f1;
    --cover-teal: #0c4054;
    --ink-light: #ffffff;
    --ink-soft: #e4eef2;
    --rule-blue: #1d6f8f;
    --photo-glow: #f4ecd2;
    --photo-sky: #5aa9dc;
    --photo-blue: #2a6fa8;
    --photo-earth: #7a6a3c;
    --sans: "Questrial", "Century Gothic", sans-serif;
    --script: "Kaushan Script", "Brush Script MT", cursive;
  }
  * { box-sizing: border-box; margin: 0; padding: 0; }
  html, body {
    width: 1200px; height: 800px; overflow: hidden;
    background: var(--page-bg);
  }
  .cover-wrap {
    position: absolute; left: 99px; top: 40px;
    width: 1002px; height: 723px;
    background: var(--cover-teal);
    color: var(--ink-light);
    font-family: var(--sans);
    overflow: hidden;
  }

  /* ---------- Back panel ---------- */
  .back-panel { position: absolute; left: 0; top: 0; width: 490px; height: 100%; }
  .back-title { position: absolute; left: 26px; top: 20px; width: 186px; }
  .back-title .line-sans { font-size: 18px; line-height: 19px; display: block; }
  .back-title .line-sans.indent { padding-left: 34px; }
  .back-title .line-script {
    font-family: var(--script); font-weight: 400; font-size: 32px; line-height: 36px; display: block;
  }
  .back-title .line-script.indent { padding-left: 52px; }
  .back-title .tagline-small {
    font-size: 9.5px; line-height: 12px; text-align: center; margin-top: 4px; color: var(--ink-soft);
  }
  .copy { font-size: 12.6px; line-height: 16px; text-align: justify; color: var(--ink-light); }
  .copy-intro { position: absolute; left: 222px; top: 28px; width: 246px; }
  .copy-intro-tail { position: absolute; left: 28px; top: 172px; width: 440px; }
  .copy-second { position: absolute; left: 28px; top: 222px; width: 440px; }
  .section-rule {
    position: absolute; left: 28px; top: 362px; width: 440px; height: 2px;
    background: linear-gradient(90deg, transparent, var(--rule-blue) 20%, var(--rule-blue) 80%, transparent);
  }
  .author-photo {
    position: absolute; left: 28px; top: 392px; width: 120px; height: 120px; background: var(--ink-light);
  }
  .copy-bio { position: absolute; left: 162px; top: 392px; width: 306px; }
  .copy-bio-tail { position: absolute; left: 28px; top: 535px; width: 440px; }
  .copy-closing { position: absolute; left: 28px; top: 568px; width: 440px; }

  /* ---------- Spine ---------- */
  .spine { position: absolute; left: 488px; top: 0; width: 32px; height: 100%; }
  .spine-title, .spine-author { position: absolute; left: 4px; writing-mode: vertical-rl; white-space: nowrap; }
  .spine-title { top: 42px; font-size: 19px; }
  .spine-author { top: 552px; font-size: 13px; }

  /* ---------- Front panel ---------- */
  .front-panel { position: absolute; left: 520px; top: 0; width: 482px; height: 100%; }
  .cover-photo {
    position: absolute; left: 0; top: 270px; width: 482px; height: 453px;
    background:
      radial-gradient(circle at 50% 42%, var(--photo-glow) 0 14%, #cfe3ef 20%, var(--photo-sky) 32%, var(--photo-blue) 46%, rgba(42,111,168,0) 58%),
      linear-gradient(180deg, var(--cover-teal) 0%, #31566a 22%, var(--photo-earth) 55%, #3b4a3a 80%, #8a6a34 100%);
  }
  .author-band { position: absolute; left: 0; top: 34px; width: 482px; height: 2px; background: var(--ink-light); }
  .author-box {
    position: absolute; left: 80px; top: 16px; width: 316px; height: 39px;
    border: 2px solid var(--ink-light); border-radius: 10px;
    background: var(--cover-teal);
    font-size: 20px; letter-spacing: 0.2px; text-align: center; line-height: 35px;
  }
  .front-title { font-weight: 400; }
  .front-title .line-sans { position: absolute; font-size: 36px; line-height: 1; white-space: nowrap; }
  .front-title .line-one { left: 92px; top: 70px; }
  .front-title .line-two { left: 150px; top: 108px; }
  .front-title .line-script {
    position: absolute; font-family: var(--script); font-weight: 400; font-size: 70px; line-height: 1; white-space: nowrap;
  }
  .front-title .line-three { left: 110px; top: 140px; }
  .front-title .line-four { left: 200px; top: 200px; }
  .front-tagline {
    position: absolute; left: 0; width: 482px; top: 688px; text-align: center; font-size: 15.5px;
  }
</style>
</head>
<body>
  <div class="cover-wrap">

    <section class="back-panel">
      <div class="back-title">
        <span class="line-sans">Where the</span>
        <span class="line-sans indent">Quiet Gardens</span>
        <span class="line-script">Grow</span>
        <span class="line-script indent">Again</span>
        <p class="tagline-small">Walking through the loss of a child<br>with honesty and hope</p>
      </div>
      <p class="copy copy-intro">Lorem ipsum dolor sit amet, consectetur adipiscing elit, sed do eiusmod tempor incididunt ut labore et dolore magna aliqua. Ut enim ad minim veniam, quis nostrud exercitation ullamco laboris nisi ut aliquip ex ea commodo consequat. Duis aute irure dolor in reprehenderit in voluptate velit esse cillum dolore eu fugiat nulla pariatur. Excepteur sint oc-</p>
      <p class="copy copy-intro-tail">caecat cupidatat non proident, sunt in culpa qui officia deserunt mollit anim id est laborum.</p>
      <p class="copy copy-second">Lorem ipsum dolor sit amet, consectetur adipiscing elit, sed do eiusmod tempor incididunt ut labore et dolore magna aliqua. Ut enim ad minim veniam, quis nostrud exercitation ullamco laboris nisi ut aliquip ex ea commodo consequat. Duis aute irure dolor in reprehenderit in voluptate velit esse cillum dolore eu fugiat nulla pariatur. Excepteur sint occaecat cupidatat non proident, sunt in culpa qui officia deserunt mollit anim id est laborum.</p>
      <div class="section-rule"></div>
      <div class="author-photo" role="img" aria-label="Author photograph placeholder"></div>
      <p class="copy copy-bio">Lorem ipsum dolor sit amet, consectetur adipiscing elit, sed do eiusmod tempor incididunt ut labore et dolore magna aliqua. Ut enim ad minim veniam, quis nostrud exercitation ullamco laboris nisi ut aliquip ex ea commodo consequat. Duis aute irure dolor in reprehenderit in voluptate velit esse cillum dolore eu fugiat nulla pariatur. Excepteur sint occaecat cupidatat non proident, sunt in culpa qui officia deserunt mollit anim id est</p>
      <p class="copy copy-bio-tail">laborum.</p>
      <p class="copy copy-closing">Lorem ipsum dolor sit amet, consectetur adipiscing elit, sed do eiusmod tempor incididunt ut labore et dolore magna aliqua. Ut enim ad minim veniam, quis nostrud exercitation ullamco laboris nisi ut aliquip ex ea commodo consequat. Duis aute irure dolor in reprehenderit in volup-</p>
    </section>

    <section class="spine">
      <span class="spine-title">Where the Quiet Gardens Grow Again</span>
      <span class="spine-author">by WHITCOMBE HALE</span>
    </section>

    <section class="front-panel">
      <div class="cover-photo" role="img" aria-label="Swirling circular landscape of blue water and golden hills around a glowing centre with a green butterfly"></div>
      <div class="author-band"></div>
      <div class="author-box">MARLA WHITCOMBE HALE</div>
      <h1 class="front-title">
        <span class="line-sans line-one">Where the</span>
        <span class="line-sans line-two">Quiet Gardens</span>
        <span class="line-script line-three">Grow</span>
        <span class="line-script line-four">Again</span>
      </h1>
      <p class="front-tagline">Walking through the loss of a child with honesty and hope</p>
    </section>

  </div>
</body>
</html>
```